One Page Template Mobile Reviews

Move our reviews web site template to a mobile template.
We produce a review web site for our customers like this one:

http://dental.brindlequeue.net/surveys57461/KoT31WQZ/surveys.htm

These are X pages with the exact same format.
We need to have this format adapted to an iPhone format.

So this is really ONE page project!

Target Market(s)

Patients looking for feedback on a particular practice

Industry/Entity Type

Dental

Requirements
Must have
• Running on iPhone using the HTML "viewport" tags

```html
<!DOCTYPE html>
<html lang="en">
<head>
<meta charset="utf-8">
<meta name="viewport" content="width=device-width, initial-scale=1">
<title>BrindleQueue – Mobile Reviews Template</title>
<link rel="stylesheet" href="https://fonts.googleapis.com/css2?family=Arimo:wght@400;700&display=swap">
<style>
:root{
  --page-bg-top:#f4f4f4;
  --page-bg-bottom:#d9d9d9;
  --screen-bg:#ffffff;
  --status-bg:#0d0d0d;
  --status-text:#e6e6e6;
  --band-blue:#8fb2d6;
  --band-text:#ffffff;
  --count-yellow:#f5e13a;
  --navy:#1d2b45;
  --navy-light:#2c3d5c;
  --link-blue:#4d86c6;
  --percent-blue:#1f4f8f;
  --text-dark:#1b1b1b;
  --text-mid:#555555;
  --text-soft:#8a8a8a;
  --rule:#d6d6d6;
  --card-body:#ececec;
  --row-tint:#e8eef6;
  --button-dark:#222222;
  --button-gray:#9a9a9a;
  --brand-red:#9b2a2a;
}
*{box-sizing:border-box;margin:0;padding:0}
html,body{width:1200px;height:768px;overflow:hidden}
body{
  font-family:"Arimo",Helvetica,Arial,sans-serif;
  background:linear-gradient(var(--page-bg-top),var(--page-bg-bottom));
  color:var(--text-dark);
}
.sprites{position:absolute;width:0;height:0}
.stage{
  display:flex;justify-content:center;gap:60px;
  padding-top:136px;
}
.screen{
  width:330px;height:495px;overflow:hidden;
  background:var(--screen-bg);
  box-shadow:0 8px 24px rgba(0,0,0,.18);
  position:relative;
}
.status-bar{
  height:20px;background:var(--status-bg);color:var(--status-text);
  display:flex;align-items:center;justify-content:space-between;
  padding:0 8px;font-size:11px;font-weight:700;letter-spacing:.3px;
}
.status-bar .carrier{display:flex;align-items:center;gap:4px}
.status-bar svg{display:block}
.count-band{
  height:24px;background:var(--band-blue);color:var(--band-text);
  font-size:11px;font-weight:700;display:flex;align-items:center;justify-content:center;gap:5px;
  text-shadow:0 1px 0 rgba(0,0,0,.15);
}
.count-band .count{color:var(--count-yellow)}
.stars{display:flex;gap:3px}
.stars svg{width:18px;height:18px}
.stars.small{gap:2px}
.stars.small svg{width:14px;height:14px}
.review{border-bottom:1px solid var(--rule)}
.review-head{padding:10px 12px 6px}
.reviewer{display:flex;gap:8px;align-items:center}
.avatar{width:28px;height:30px;background:linear-gradient(#e2e2e2,#bdbdbd);border-radius:3px}
.reviewer-name{font-size:12px;color:var(--text-mid)}
.reviewer-name .place{color:var(--link-blue)}
.review-date{font-size:9px;color:var(--text-soft)}
.review-title{font-size:14px;font-weight:700;margin:6px 0 6px}
.score-row{display:flex;align-items:center;gap:12px}
.percent{font-size:15px;font-weight:700;color:var(--percent-blue)}
.toggle{
  margin-left:auto;width:22px;height:15px;border-radius:3px;
  background:linear-gradient(#bcbcbc,var(--button-gray));
  display:flex;align-items:center;justify-content:center;
}
.review-body{
  background:var(--card-body);padding:8px 12px 12px;
  font-size:9.5px;line-height:1.35;color:var(--text-mid);
}
.brand-bar{
  height:34px;display:flex;align-items:center;justify-content:center;gap:6px;
  border-bottom:1px solid var(--rule);
}
.brand-dot{width:9px;height:9px;border-radius:50%;background:var(--link-blue)}
.brand-name{font-size:15px;color:var(--brand-red);font-weight:400}
.profile{
  background:linear-gradient(var(--navy-light),var(--navy));color:#fff;
  padding:12px 12px 14px;
}
.profile-top{display:flex;gap:12px}
.portrait{
  width:84px;height:84px;border:3px solid #fff;
  background:linear-gradient(#6f86a6,#3e4f6b);
}
.doctor-name{font-size:17px;font-weight:700;line-height:1.1}
.doctor-title{font-size:13px;font-weight:700;margin-bottom:9px}
.doctor-address{font-size:10px;line-height:1.4;color:#dfe4ec;font-style:normal}
.profile-score{display:flex;align-items:center;margin-top:12px}
.profile-score .stars svg{width:24px;height:24px}
.score-box{margin-left:auto;text-align:right}
.score-big{font-size:28px;font-weight:400}
.score-sub{font-size:9.5px;color:#cfd6e2}
.details{padding:10px 16px 0}
.detail-row{
  display:flex;gap:12px;padding:5px 0;border-bottom:1px solid var(--rule);
  align-items:flex-start;
}
.detail-label{width:68px;text-align:right;font-size:12px;color:var(--text-dark)}
.detail-value{font-size:14px;color:var(--text-mid)}
.hours{display:grid;grid-template-columns:62px auto;font-size:9.5px;color:var(--text-mid);row-gap:2px;padding-top:2px}
.book{
  display:flex;align-items:center;justify-content:center;gap:12px;padding:12px 0 10px;
}
.book-link{font-size:12px;color:var(--text-dark);text-decoration:underline}
.book-button{
  width:28px;height:22px;border-radius:4px;background:var(--button-dark);
  display:flex;align-items:center;justify-content:center;
}
.bottom-band{position:absolute;left:0;right:0;bottom:0}
.survey-rows{margin-top:6px;border-top:1px solid var(--rule)}
.survey-row{
  display:flex;justify-content:space-between;align-items:center;
  font-size:9.5px;padding:3px 0 3px;border-bottom:1px solid var(--rule);
}
.survey-row:nth-child(odd){background:var(--row-tint)}
.survey-row .stars{padding-right:4px}
.pager{padding:10px 14px 0;text-align:center}
.to-top{font-size:12px;text-decoration:underline;display:block;margin-bottom:10px}
.pager-row{display:flex;align-items:center;justify-content:space-between}
.pager-btn{
  font-size:9.5px;border-radius:10px;padding:4px 10px;color:#fff;
  display:flex;align-items:center;gap:4px;
}
.pager-btn.prev{background:#c4c4c4}
.pager-btn.next{background:var(--button-dark)}
.page-count{font-size:11px;font-weight:700}
.page-grid{
  display:grid;grid-template-columns:repeat(9,1fr);row-gap:4px;
  font-size:11px;margin-top:14px;text-align:left;
}
.page-grid .current{color:var(--brand-red)}
</style>
</head>
<body>

<svg class="sprites" aria-hidden="true">
  <defs>
    <linearGradient id="half-fill">
      <stop offset="50%" stop-color="#f4d31c"/>
      <stop offset="50%" stop-color="#ffffff"/>
    </linearGradient>
    <symbol id="star" viewBox="0 0 24 24">
      <path d="M12 1.5l3.1 6.9 7.4.7-5.6 5 1.7 7.4L12 17.7l-6.6 3.8 1.7-7.4-5.6-5 7.4-.7z" fill="#f4d31c" stroke="#c9a900" stroke-width=".8"/>
    </symbol>
    <symbol id="star-half" viewBox="0 0 24 24">
      <path d="M12 1.5l3.1 6.9 7.4.7-5.6 5 1.7 7.4L12 17.7l-6.6 3.8 1.7-7.4-5.6-5 7.4-.7z" fill="url(#half-fill)" stroke="#c9a900" stroke-width=".8"/>
    </symbol>
    <symbol id="signal" viewBox="0 0 12 12">
      <g fill="#e6e6e6"><rect x="0" y="8" width="2" height="3"/><rect x="3" y="6" width="2" height="5"/><rect x="6" y="4" width="2" height="7"/><rect x="9" y="2" width="2" height="9"/></g>
    </symbol>
    <symbol id="chevron-down" viewBox="0 0 10 6"><path d="M0 0h10L5 6z" fill="#fff"/></symbol>
    <symbol id="chevron-up" viewBox="0 0 10 6"><path d="M0 6h10L5 0z" fill="#fff"/></symbol>
  </defs>
</svg>

<main class="stage">

  <section class="screen reviews-list">
    <div class="status-bar">
      <span class="carrier"><svg width="12" height="11" viewBox="0 0 12 12"><use href="#signal"/></svg>CARRIER</span>
      <svg width="8" height="10" viewBox="0 0 8 10"><rect x="0" y="4" width="8" height="6" fill="#e6e6e6"/><path d="M2 4V2.5a2 2 0 0 1 4 0V4" stroke="#e6e6e6" fill="none" stroke-width="1.2"/></svg>
      <svg width="20" height="9" viewBox="0 0 20 9"><rect x=".5" y=".5" width="17" height="8" fill="none" stroke="#e6e6e6"/><rect x="2" y="2" width="14" height="5" fill="#e6e6e6"/><rect x="18" y="3" width="2" height="3" fill="#e6e6e6"/></svg>
    </div>
    <div class="count-band"><span class="count">747</span> Certified Patients Reviews &amp; Surveys</div>

    <article class="review">
      <div class="review-head">
        <div class="reviewer">
          <div class="avatar" role="img" aria-label="Reviewer avatar placeholder"></div>
          <div><div class="reviewer-name">MaraT <span class="place">Birch Hollow</span></div><div class="review-date">October 05, 2012</div></div>
        </div>
        <h3 class="review-title">I am especially grateful that ...</h3>
        <div class="score-row">
          <div class="stars"><svg><use href="#star"/></svg><svg><use href="#star"/></svg><svg><use href="#star"/></svg><svg><use href="#star"/></svg><svg><use href="#star"/></svg></div>
          <span class="percent">100.00%</span>
          <span class="toggle"><svg width="9" height="5"><use href="#chevron-down"/></svg></span>
        </div>
      </div>
      <p class="review-body">I am especially grateful that Dr. Marchetti saw and immediately fixed a cavity that would have been a root canal if it had been left for a future appointment.</p>
    </article>

    <article class="review">
      <div class="review-head">
        <div class="reviewer">
          <div class="avatar" role="img" aria-label="Anonymous reviewer avatar placeholder"></div>
          <div><div class="reviewer-name">Anonymous VA</div><div class="review-date">October 04, 2012</div></div>
        </div>
        <h3 class="review-title">Wonderful service and wonderful ...</h3>
        <div class="score-row">
          <div class="stars"><svg><use href="#star"/></svg><svg><use href="#star"/></svg><svg><use href="#star"/></svg><svg><use href="#star"/></svg><svg><use href="#star"/></svg></div>
          <span class="percent">100.00%</span>
          <span class="toggle"><svg width="9" height="5"><use href="#chevron-down"/></svg></span>
        </div>
      </div>
      <p class="review-body">Wonderful service and wonderful dentist and staff these many long years!! :0)</p>
    </article>

    <article class="review">
      <div class="review-head">
        <div class="reviewer">
          <div class="avatar" role="img" aria-label="Reviewer avatar placeholder"></div>
          <div><div class="reviewer-name">TomK <span class="place">Aspen Vale</span></div><div class="review-date">September 27, 2012</div></div>
        </div>
        <h3 class="review-title">Love my dentist (and Tessa)! ...</h3>
        <div class="score-row">
          <div class="stars"><svg><use href="#star"/></svg><svg><use href="#star"/></svg><svg><use href="#star"/></svg><svg><use href="#star"/></svg><svg><use href="#star"/></svg></div>
          <span class="percent">100.00%</span>
          <span class="toggle"><svg width="9" height="5"><use href="#chevron-down"/></svg></span>
        </div>
      </div>
      <p class="review-body">Love my dentist (and Tessa)!</p>
    </article>
  </section>

  <section class="screen profile-screen">
    <div class="status-bar">
      <span class="carrier"><svg width="12" height="11" viewBox="0 0 12 12"><use href="#signal"/></svg>CARRIER</span>
      <svg width="8" height="10" viewBox="0 0 8 10"><rect x="0" y="4" width="8" height="6" fill="#e6e6e6"/><path d="M2 4V2.5a2 2 0 0 1 4 0V4" stroke="#e6e6e6" fill="none" stroke-width="1.2"/></svg>
      <svg width="20" height="9" viewBox="0 0 20 9"><rect x=".5" y=".5" width="17" height="8" fill="none" stroke="#e6e6e6"/><rect x="2" y="2" width="14" height="5" fill="#e6e6e6"/><rect x="18" y="3" width="2" height="3" fill="#e6e6e6"/></svg>
    </div>
    <header class="brand-bar"><span class="brand-dot"></span><span class="brand-name">BrindleQueue</span></header>

    <div class="profile">
      <div class="profile-top">
        <div class="portrait" role="img" aria-label="Portrait photo of the dentist"></div>
        <div>
          <h1 class="doctor-name">Daniel Marchetti</h1>
          <div class="doctor-title">DDS, FAGD</div>
          <address class="doctor-address">4120 Hollis Ridge Road Suite 310<br>Fairbrook, VA 22190</address>
        </div>
      </div>
      <div class="profile-score">
        <div class="stars"><svg><use href="#star"/></svg><svg><use href="#star"/></svg><svg><use href="#star"/></svg><svg><use href="#star"/></svg><svg><use href="#star-half"/></svg></div>
        <div class="score-box"><div class="score-big">98.19%</div><div class="score-sub">747 Reviews &amp; Surveys</div></div>
      </div>
    </div>

    <div class="details">
      <div class="detail-row"><span class="detail-label">Website</span><span class="detail-value">www.drmarchetti-dental.com</span></div>
      <div class="detail-row"><span class="detail-label">Phone</span><span class="detail-value">(555) 014-2750</span></div>
      <div class="detail-row"><span class="detail-label">Office hours</span>
        <div class="hours">
          <span>Monday</span><span>7:30 AM 2:00 PM</span>
          <span>Tuesday</span><span>7:30 AM 5:00 PM</span>
          <span>Wednesday</span><span>7:30 AM 5:00 PM</span>
          <span>Thursday</span><span>7:30 AM 1:00 PM</span>
        </div>
      </div>
    </div>
    <div class="book">
      <span class="book-link">Book An Appointment Entirely Online</span>
      <span class="book-button"><svg width="10" height="14" viewBox="0 0 10 14"><rect x=".7" y=".7" width="8.6" height="12.6" rx="4.3" fill="#fff"/><line x1="5" y1="2.5" x2="5" y2="5.5" stroke="#222" stroke-width="1.2"/></svg></span>
    </div>
    <div class="count-band bottom-band"><span class="count">747</span> Certified Patients Reviews &amp; Surveys</div>
  </section>

  <section class="screen survey-detail">
    <div class="status-bar">
      <span class="carrier"><svg width="12" height="11" viewBox="0 0 12 12"><use href="#signal"/></svg>CARRIER</span>
      <svg width="8" height="10" viewBox="0 0 8 10"><rect x="0" y="4" width="8" height="6" fill="#e6e6e6"/><path d="M2 4V2.5a2 2 0 0 1 4 0V4" stroke="#e6e6e6" fill="none" stroke-width="1.2"/></svg>
      <svg width="20" height="9" viewBox="0 0 20 9"><rect x=".5" y=".5" width="17" height="8" fill="none" stroke="#e6e6e6"/><rect x="2" y="2" width="14" height="5" fill="#e6e6e6"/><rect x="18" y="3" width="2" height="3" fill="#e6e6e6"/></svg>
    </div>
    <article class="review">
      <div class="review-head">
        <div class="reviewer">
          <div class="avatar" role="img" aria-label="Reviewer avatar placeholder"></div>
          <div><div class="reviewer-name">JuneW</div><div class="review-date">August 02, 2012</div></div>
        </div>
        <h3 class="review-title">I was very pleased with how ...</h3>
        <div class="score-row">
          <div class="stars"><svg><use href="#star"/></svg><svg><use href="#star"/></svg><svg><use href="#star"/></svg><svg><use href="#star"/></svg><svg><use href="#star"/></svg></div>
          <span class="percent">100.00%</span>
          <span class="toggle"><svg width="9" height="5"><use href="#chevron-up"/></svg></span>
        </div>
        <div class="survey-rows">
          <div class="survey-row"><span>Overall satisfaction (1x)</span><div class="stars small"><svg><use href="#star"/></svg><svg><use href="#star"/></svg><svg><use href="#star"/></svg><svg><use href="#star"/></svg><svg><use href="#star"/></svg></div></div>
          <div class="survey-row"><span>Staff (4x)</span><div class="stars small"><svg><use href="#star"/></svg><svg><use href="#star"/></svg><svg><use href="#star"/></svg><svg><use href="#star"/></svg><svg><use href="#star"/></svg></div></div>
          <div class="survey-row"><span>Provider (1x)</span><div class="stars small"><svg><use href="#star"/></svg><svg><use href="#star"/></svg><svg><use href="#star"/></svg><svg><use href="#star"/></svg><svg><use href="#star"/></svg></div></div>
          <div class="survey-row"><span>Hygienist (2x)</span><div class="stars small"><svg><use href="#star"/></svg><svg><use href="#star"/></svg><svg><use href="#star"/></svg><svg><use href="#star"/></svg><svg><use href="#star"/></svg></div></div>
          <div class="survey-row"><span>Waiting Time (1x)</span><div class="stars small"><svg><use href="#star"/></svg><svg><use href="#star"/></svg><svg><use href="#star"/></svg><svg><use href="#star"/></svg><svg><use href="#star"/></svg></div></div>
          <div class="survey-row"><span>Fees (1x)</span><div class="stars small"><svg><use href="#star"/></svg><svg><use href="#star"/></svg><svg><use href="#star"/></svg><svg><use href="#star"/></svg><svg><use href="#star"/></svg></div></div>
        </div>
      </div>
      <p class="review-body">I was very pleased with how quickly you responded, the excellent help/care, and regret only that I will not be able to stay in the neighborhood to have you complete the cap/crowns. Should I have similar problems in the future while nearby, you will be the first office I will call. I also look forward to recommending you to colleagues.</p>
    </article>
    <nav class="pager">
      <span class="to-top">Go to Top</span>
      <div class="pager-row">
        <span class="pager-btn prev">&#9664; previous</span>
        <span class="page-count">Page 1/30</span>
        <span class="pager-btn next">next &#9654;</span>
      </div>
      <div class="page-grid">
        <span class="current">[1]</span><span>[2]</span><span>[3]</span><span>[4]</span><span>[5]</span><span>[6]</span><span>[7]</span><span>[8]</span><span>[9]</span>
        <span>[10]</span><span>[11]</span><span>[12]</span><span>[13]</span><span>[14]</span><span>[15]</span><span>[16]</span><span>[17]</span><span>[18]</span>
        <span>[19]</span><span>[20]</span><span>[21]</span><span>[22]</span><span>[23]</span><span>[24]</span><span>[25]</span><span>[26]</span><span>[27]</span>
      </div>
    </nav>
  </section>

</main>
</body>
</html>
```